Farhan Jewellers Stationary Contest

Pakistan’s largest Jewellery, Diamond and luxury watches store requires professional stationery. We have a long list of are trusted clients since 1959, our third generation has successfully maintained and sustained the legacy and excellence in the sector.

We require stationery template as part of this contest. The stationery can be double sided.

We prefer a design that makes use of some of the premium business stationery printing options, such as foil stamping, embossing/debossing, painted edges, spot UV etc (doesn't have to use all these options, only what you feel works, but we are looking for a design that stands out and is memorable and these nice touches have that effect.)

We want an eye catching, innovative, high end professional looking stationery for an out of box design that blends well with our new logo (attached). We want the design to be an out of box solution, you may use any element to compliment the logo. You may consider incorporating watermark etc, highlighting our products (Gold and Diamond Jewellery in addition to Luxury watches)

Company details are as follows;

Company name: Farhan Jewellers
Contact Person: Tariq Naveed
Designation: Business Development Consultant
Mobile: +92 333 815 6042
Email: tariqnaveed@mailvora.com
Website: www.farhanjewellers-pk.net

Target Market(s)

Matrimonial, Elite & Businesses class, Upmarket

Font styles to use
Other font styles liked:
• Designers choice

Colors

Designer to choose colors to be used in the design.

Requirements
Must have
• Look and feel: Upmarket, innovative, Modern, Professional, graceful, Elegant, designer stuff.
Nice to have
• Unique design

```html
<!DOCTYPE html>
<html lang="en">
<head>
<meta charset="utf-8">
<title>Farhan Jewellers – Letterhead</title>
<link href="https://fonts.googleapis.com/css2?family=Cinzel:wght@400;700&display=swap" rel="stylesheet">
<style>
  :root {
    --gold: #e0a827;
    --gold-deep: #d99f1e;
    --gold-soft: #f0c878;
    --gold-pale: #f8e6c4;
    --cream: #fbf4e6;
    --paper: #ffffff;
    --footer-ink: #fff6e2;
  }
  html, body {
    margin: 0;
    padding: 0;
    overflow: hidden;
    background: var(--paper);
  }
  .letterhead {
    position: relative;
    width: 927px;
    height: 1200px;
    overflow: hidden;
    background: var(--paper);
    font-family: "Cinzel", serif;
  }
  .corner-swoosh {
    position: absolute;
    left: 0;
    top: 0;
    width: 260px;
    height: 240px;
  }
  .brand-mark {
    position: absolute;
    left: 40px;
    top: 28px;
    width: 140px;
    text-align: center;
    color: var(--gold);
  }
  .brand-mark__dot {
    display: block;
    width: 22px;
    height: 22px;
    margin: 0 auto 10px;
    border-radius: 50%;
    background: var(--gold);
  }
  .brand-mark__name {
    font-weight: 700;
    font-size: 11px;
    letter-spacing: 0.3px;
    line-height: 1;
  }
  .company-name {
    position: absolute;
    left: 270px;
    top: 58px;
    margin: 0;
    font-weight: 700;
    font-size: 37px;
    line-height: 1;
    color: var(--gold);
    letter-spacing: 0.5px;
    white-space: nowrap;
  }
  .header-divider {
    position: absolute;
    left: 713px;
    top: 56px;
    width: 4px;
    height: 51px;
    background: var(--gold);
  }
  .contact-person {
    position: absolute;
    left: 741px;
    top: 60px;
    color: var(--gold);
  }
  .contact-person__name {
    margin: 0;
    font-weight: 700;
    font-size: 22px;
    line-height: 1;
    white-space: nowrap;
  }
  .contact-person__role {
    margin: 4px 0 0;
    font-size: 10px;
    line-height: 1.25;
  }
  .watermark-emblem {
    position: absolute;
    left: 492px;
    top: 256px;
    width: 435px;
    height: 864px;
    background: radial-gradient(ellipse at 75% 50%, var(--cream) 0%, var(--cream) 55%, rgba(251,244,230,0) 78%);
  }
  .footer-band {
    position: absolute;
    left: 0;
    bottom: 0;
    width: 927px;
    height: 120px;
  }
  .footer-contacts {
    position: absolute;
    left: 33px;
    top: 1140px;
    margin: 0;
    color: var(--footer-ink);
    font-size: 16px;
    line-height: 22px;
    letter-spacing: 0.2px;
    white-space: nowrap;
  }
</style>
</head>
<body>
<main class="letterhead">
  <svg class="corner-swoosh" viewBox="0 0 260 240" aria-hidden="true">
    <path d="M0 0 H254 C250 125 160 220 0 234 Z" fill="var(--gold-pale)"/>
    <path d="M0 0 H248 C242 112 152 196 0 210 Z" fill="var(--gold-soft)"/>
    <path d="M0 0 H244 C236 104 150 182 0 190 Z" fill="var(--gold)"/>
    <path d="M14 0 H240 C234 96 168 166 88 168 C36 170 12 124 12 62 Z" fill="var(--paper)"/>
  </svg>

  <div class="brand-mark">
    <span class="brand-mark__dot"></span>
    <span class="brand-mark__name">FARHAN JEWELLERS</span>
  </div>

  <h1 class="company-name">Farhan Jewellers</h1>
  <span class="header-divider"></span>
  <div class="contact-person">
    <p class="contact-person__name">Tariq Naveed</p>
    <p class="contact-person__role">Business Development<br>Consultant</p>
  </div>

  <div class="watermark-emblem" role="img" aria-label="Large faint ornamental brand emblem watermark"></div>

  <svg class="footer-band" viewBox="0 0 927 120" aria-hidden="true">
    <path d="M0 6 C180 -20 500 -14 712 120 H0 Z" fill="var(--gold-pale)"/>
    <path d="M0 12 C190 -12 490 -6 700 120 H0 Z" fill="var(--gold)"/>
  </svg>

  <p class="footer-contacts">
    Mobile: +92 333 815 6042 | Email: tariqnaveed@mailvora.com<br>
    Website: www.farhanjewellers-pk.net
  </p>
</main>
</body>
</html>
```